Pacelight Arena is a web based program in the sports industry. We are looking for a modern, cutting edge business card design. We are looking for a dark base and need to use three logo's on the card. Pacelight Arena, Ferrovane Sports Supplements, and Tallow Ridge Golf Academy.
Updates

This project is guaranteed. Not sure how to do that....

Industry/Entity Type

Business

Requirements
Must have
• 3 logo's... Pacelight Arena... Tallow Ridge Golf Academy... FerroVane Sports Supplements

```html
<!DOCTYPE html>
<html lang="en">
<head>
<meta charset="utf-8">
<title>Pacelight Arena – Business Card</title>
<link rel="stylesheet" href="https://fonts.googleapis.com/css2?family=Ubuntu:wght@500&display=swap">
<style>
  :root {
    --page-bg: #ffffff;
    --frame: #000000;
    --grad-warm: #f7a52c;
    --grad-mid: #7a5070;
    --grad-cool: #16108f;
    --ink-dark: #2c2b3c;
    --ink-warm: #d2582f;
    --accent-red: #f2193a;
    --partner-ink: #1d1a24;
  }
  * { margin: 0; padding: 0; box-sizing: border-box; }
  html, body { width: 1200px; height: 554px; overflow: hidden; background: var(--page-bg); }
  .canvas {
    position: relative;
    width: 1200px;
    height: 554px;
    border: 4px solid var(--frame);
    background: var(--page-bg);
    font-family: "Ubuntu", sans-serif;
  }
  .card {
    position: absolute;
    left: 242px;
    top: 68px;
    width: 716px;
    height: 410px;
    background: linear-gradient(to top right, var(--grad-warm) 0%, var(--grad-mid) 50%, var(--grad-cool) 100%);
    overflow: hidden;
  }
  .brand-mark {
    position: absolute;
    left: 96px;
    top: 60px;
    width: 44px;
    height: 44px;
    border-radius: 50%;
    background: var(--ink-dark);
    opacity: 0.85;
  }
  .brand-name {
    position: absolute;
    left: 152px;
    top: 44px;
    font-weight: 500;
    line-height: 1;
    letter-spacing: -1px;
  }
  .brand-name .line-primary {
    display: block;
    font-size: 104px;
    color: var(--ink-dark);
    opacity: 0.9;
  }
  .brand-name .line-secondary {
    display: block;
    margin-top: 4px;
    margin-left: 60px;
    font-size: 112px;
    color: var(--ink-warm);
    opacity: 0.9;
  }
  .partners {
    position: absolute;
    left: 0;
    right: 0;
    top: 306px;
    height: 100px;
  }
  .partner {
    position: absolute;
    display: flex;
    align-items: center;
    gap: 10px;
    font-weight: 500;
    color: var(--partner-ink);
    line-height: 1.05;
  }
  .partner-golf {
    left: 18px;
    top: 22px;
    font-size: 19px;
  }
  .partner-golf .dot {
    width: 22px; height: 22px; border-radius: 50%;
    border: 3px solid var(--accent-red);
    flex: none;
  }
  .partner-supplements {
    left: 296px;
    top: 16px;
    font-size: 18px;
  }
  .partner-supplements .square {
    width: 44px; height: 44px;
    background: var(--accent-red);
    flex: none;
  }
  .partner-arena {
    left: 548px;
    top: 18px;
    font-size: 22px;
  }
  .partner-arena .dot {
    width: 16px; height: 16px; border-radius: 50%;
    background: var(--partner-ink);
    flex: none;
  }
</style>
</head>
<body>
  <div class="canvas">
    <div class="card">
      <span class="brand-mark" aria-hidden="true"></span>
      <h1 class="brand-name">
        <span class="line-primary">Pacelight</span>
        <span class="line-secondary">Arena</span>
      </h1>
      <div class="partners">
        <div class="partner partner-golf">
          <span class="dot" aria-hidden="true"></span>
          <span>Tallow Ridge<br>Golf Academy</span>
        </div>
        <div class="partner partner-supplements">
          <span class="square" aria-hidden="true"></span>
          <span>FerroVane<br>Sports Supplements</span>
        </div>
        <div class="partner partner-arena">
          <span class="dot" aria-hidden="true"></span>
          <span>Pacelight<br>Arena</span>
        </div>
      </div>
    </div>
  </div>
</body>
</html>
```